Commercial Insurance Agency needs a design for a trade show retractable display.

We need a design for a retractable banner or display for a trade show. We are a commercial insurance agency that specializes in placing and servicing workers comp insurance for large companies. We want to use our company colors which are orange, grey and charcoal.

Font styles to use
Sans Serif

Requirements
Must have
• Our orange color that is on the style sheet should be the secondary color...we don't want the whole thing to be orange

```html
<!DOCTYPE html>
<html lang="en">
<head>
<meta charset="UTF-8">
<title>TRUEVIEW – Work Comp Re-Audit Services Display</title>
<link href="https://fonts.googleapis.com/css2?family=Roboto+Condensed:wght@300;400;700&display=swap" rel="stylesheet">
<style>
  :root {
    --orange: #f05a1e;
    --charcoal: #4f5052;
    --grey-mid: #6f7072;
    --grey-light: #a3a4a6;
    --circle: #e4e4e5;
    --icon: #4f5052;
    --panel: #ffffff;
    --body-text: #6d6e70;
    --white: #ffffff;
  }
  * { margin: 0; padding: 0; box-sizing: border-box; }
  html, body {
    width: 1200px; height: 2939px; overflow: hidden;
    background: var(--white);
    font-family: "Roboto Condensed", Arial, sans-serif;
  }
  .banner { position: relative; width: 1200px; height: 2939px; overflow: hidden; }

  .hero {
    position: absolute; left: 0; top: 0; width: 1200px; height: 1370px;
    background:
      linear-gradient(180deg, rgba(0,0,0,0) 45%, rgba(20,18,16,0.55) 100%),
      linear-gradient(100deg, #6b6256 0%, #8c8273 30%, #a39680 55%, #7d6f5e 80%, #5d5247 100%);
  }
  .brand-name {
    position: absolute; right: 70px; top: 270px;
    font-weight: 700; font-size: 96px; letter-spacing: 3px; color: var(--white); line-height: 1;
  }

  .headline {
    position: absolute; right: 70px; top: 850px; text-align: right;
    color: var(--white); font-weight: 700; font-size: 138px; line-height: 1.0; letter-spacing: -1px;
    text-transform: uppercase;
  }
  .rule { position: absolute; height: 8px; background: var(--orange); }
  .rule-left { left: 0; top: 1155px; width: 430px; }
  .rule-right { right: 0; top: 1155px; width: 40px; }
  .subhead {
    position: absolute; right: 70px; top: 1215px;
    color: var(--white); font-weight: 400; font-size: 58px; letter-spacing: 1px; text-transform: uppercase;
  }

  .services { position: absolute; left: 0; top: 1370px; width: 1200px; height: 1440px; }
  .service { display: flex; height: 480px; }
  .service-icon-col {
    width: 465px; display: flex; align-items: center; justify-content: center;
  }
  .service:nth-child(1) .service-icon-col { background: var(--charcoal); }
  .service:nth-child(2) .service-icon-col { background: var(--grey-mid); }
  .service:nth-child(3) .service-icon-col { background: var(--grey-light); }
  .icon-circle {
    width: 250px; height: 250px; border-radius: 50%; background: var(--circle);
    display: flex; align-items: center; justify-content: center;
  }
  .icon-circle svg { width: 120px; height: 120px; }
  .service-copy { flex: 1; background: var(--panel); padding: 110px 0 0 70px; }
  .service-title {
    color: var(--orange); font-weight: 700; font-size: 104px; line-height: 1; text-transform: uppercase; margin-bottom: 18px;
  }
  .service-text { color: var(--body-text); font-weight: 300; font-size: 50px; line-height: 1.16; }

  .contact-bar {
    position: absolute; left: 0; bottom: 0; width: 1200px; height: 129px;
    background: var(--orange); color: var(--white);
    display: flex; align-items: center; justify-content: center; gap: 30px;
    font-weight: 400; font-size: 40px; letter-spacing: 1px; white-space: nowrap;
  }
  .divider { width: 3px; height: 46px; background: var(--white); }
</style>
</head>
<body>
<main class="banner">
  <section class="hero" role="img" aria-label="Photo of a smiling worker in a hard hat and overalls holding a coffee cup in a workshop"></section>

  <div class="brand-name">TRUEVIEW</div>

  <h1 class="headline">We Audit<br>Their Audit</h1>
  <div class="rule rule-left"></div>
  <div class="rule rule-right"></div>
  <p class="subhead">Work Comp Re-Audit Services</p>

  <section class="services">
    <article class="service">
      <div class="service-icon-col">
        <div class="icon-circle">
          <svg viewBox="0 0 100 100" aria-hidden="true">
            <rect x="40" y="10" width="20" height="40" rx="8" fill="var(--icon)"/>
            <rect x="22" y="50" width="56" height="16" rx="4" fill="var(--icon)"/>
            <rect x="18" y="72" width="64" height="6" rx="2" fill="var(--icon)"/>
            <rect x="24" y="86" width="52" height="5" rx="2" fill="var(--icon)"/>
          </svg>
        </div>
      </div>
      <div class="service-copy">
        <h2 class="service-title">Compliance</h2>
        <p class="service-text">Training and Certifications<br>HR and Safety Onsite<br>Compliance Audits</p>
      </div>
    </article>
    <article class="service">
      <div class="service-icon-col">
        <div class="icon-circle">
          <svg viewBox="0 0 100 100" aria-hidden="true">
            <rect x="8" y="20" width="70" height="42" rx="3" fill="none" stroke="var(--icon)" stroke-width="6"/>
            <circle cx="43" cy="41" r="9" fill="var(--icon)"/>
            <rect x="8" y="68" width="70" height="5" fill="var(--icon)"/>
            <rect x="8" y="78" width="70" height="5" fill="var(--icon)"/>
            <ellipse cx="78" cy="70" rx="15" ry="6" fill="var(--icon)"/>
            <ellipse cx="78" cy="80" rx="15" ry="6" fill="var(--icon)"/>
          </svg>
        </div>
      </div>
      <div class="service-copy">
        <h2 class="service-title">Profit Leaks</h2>
        <p class="service-text">Detect and Correct Profit Leaks<br>Inherent in Every Work Comp<br>Program That Drives the Cost</p>
      </div>
    </article>
    <article class="service">
      <div class="service-icon-col">
        <div class="icon-circle">
          <svg viewBox="0 0 100 100" aria-hidden="true">
            <path d="M30 10 H68 L80 22 V90 H30 Z" fill="none" stroke="var(--icon)" stroke-width="6" stroke-linejoin="round"/>
            <rect x="42" y="32" width="26" height="5" fill="var(--icon)"/>
            <rect x="42" y="46" width="26" height="5" fill="var(--icon)"/>
            <rect x="50" y="74" width="18" height="5" fill="var(--icon)"/>
            <circle cx="22" cy="64" r="9" fill="none" stroke="var(--icon)" stroke-width="5"/>
            <circle cx="42" cy="64" r="9" fill="none" stroke="var(--icon)" stroke-width="5"/>
            <rect x="29" y="62" width="6" height="4" fill="var(--icon)"/>
          </svg>
        </div>
      </div>
      <div class="service-copy">
        <h2 class="service-title">Claims</h2>
        <p class="service-text">Immediate, Ongoing<br>Injury and Claims<br>Management</p>
      </div>
    </article>
  </section>

  <footer class="contact-bar">
    <span class="contact-email">info@trueviewrisk.com</span>
    <span class="divider"></span>
    <span class="contact-phone">555.014.2287</span>
    <span class="divider"></span>
    <span class="contact-web">trueviewrisk.com</span>
  </footer>
</main>
</body>
</html>
```